VELORA - Società di servizi per la lettura dei contatori acqua

Abbiamo bisogno di una brochure quadrata da 21x21 cm composta da 6 ante. La nostra società Velora.Siamo specializzati nella lettura e rilievo dei contatori dell'acqua dei condomini/immobili. Siamo una società di servizi composta da un team di professionisti ed operatori specializzati.
Offriamo soluzioni tecnologiche ed efficaci perchè tempestive e performanti.
VELORA nasce dalla richiesta del mercato di un soggetto nuovo, indipendente e soprattutto trasversale alle attuali realtà di settore.
VELORA fornisce alle società di amministrazione condominiale un servizio professionale di lettura e riparto dei consumi acqua tempestivo, preciso ed efficace.
VELORA propone un servizio innovativo sul mercato, capace di gestire la lettura ed il riparto dei consumi acqua tramite un nuovo modello di service management.
Abbiamo strutturato un servizio innovativo dedicato agli amministratori condominiali.
Effettuiamo la lettura dei consumi reali dei contatori acqua relativi alle singole utenze private e comuni.
Elaboriamo i dati raccolti in tempo reale e predisponiamo il riparto dei consumi acqua.
Gli amministratori dispongono di uno strumento tecnico che consente la corretta ed immediata ripartizione dei consumi idrici.
Il riparto dei consumi viene effettuato esclusivamente tramite letture reali, effettive e certificate delle singole utenze.

Target Market(s)

Amministratori di condominio

Font styles to use
Sans Serif

Colors
ec1f27
5c5c5c

Requirements
Must have
• Abbiamo bisogno di una brochure quadrata da 21x21 cm composta da 6 ante.

```html
<!DOCTYPE html>
<html lang="it">
<head>
<meta charset="utf-8">
<title>Velora – Brochure 6 ante</title>
<link href="https://fonts.googleapis.com/css2?family=Montserrat:wght@400;500;600;700&family=Oswald:wght@300&display=swap" rel="stylesheet">
<style>
  :root{
    --red:#ec1f27;
    --grey:#5c5c5c;
    --board:#e6e6e6;
    --white:#ffffff;
    --ink:#3a3a3a;
    --photo-a:#8e99a8;
    --photo-b:#3d4452;
  }
  *{box-sizing:border-box;margin:0;padding:0}
  html,body{width:1200px;height:1200px;overflow:hidden;background:var(--board)}
  body{position:relative;font-family:"Montserrat",sans-serif;color:var(--ink)}
  .abs{position:absolute}
  .panel{position:absolute;background:var(--white);overflow:hidden}
  .waves-dark{background:linear-gradient(180deg,#444447 0%,var(--grey) 45%,var(--grey) 100%)}
  .waves-light{background:linear-gradient(180deg,#e4e4e4 0%,#f6f6f6 100%)}
  .waves-fade{background:linear-gradient(180deg,#ffffff 60%,#f0f0f0 100%)}
  .photo{position:absolute;background:linear-gradient(135deg,var(--photo-a),var(--photo-b))}
  .photo.warm{background:linear-gradient(135deg,#c9ccd2,#6f7584 60%,#b23a3a)}
  .photo.pipe{background:linear-gradient(160deg,#e9ecef,#a9b0ba 55%,#6a6f78)}
  .illus{position:absolute;background:#d9d9d9;border-radius:50%}

  /* name set in the text font: one colour, one weight, plain square beside */
  .name{display:flex;align-items:center;gap:.3em;font-weight:600;color:var(--red);line-height:1;white-space:nowrap}
  .name::before{content:"";width:.55em;height:.55em;background:currentColor;flex:none}
  .name.center{justify-content:center}
  .name.on-dark{color:var(--white)}

  .label{font-family:"Oswald",sans-serif;font-weight:300;font-size:15px;color:#333}
  .contact{text-align:center;font-size:5.5px;line-height:1.45;color:#444}
  .socials{display:flex;gap:2px;justify-content:center;margin-bottom:4px}
  .socials span{width:10px;height:10px;background:#222;border-radius:2px}
  .num{font-weight:700;color:var(--white);font-size:38px;line-height:1}
  .title{font-weight:600;color:var(--white);font-size:15px;margin-top:6px}
  .dash{width:14px;height:6px;background:var(--red);margin:10px 0 12px}
  .body-text{font-size:4.6px;line-height:1.5;color:#e2e2e2}
  .body-text p{margin-bottom:4px}
  .body-dark{font-size:4.6px;line-height:1.5;color:#555}
  .body-dark p{margin-bottom:5px}
  .body-dark b{color:#222}
  .redbar{position:absolute;background:var(--red)}
  .foot-name{position:absolute;font-size:7px}
  .step{position:absolute;display:flex;gap:14px;align-items:flex-start}
  .step .ic{width:26px;height:26px;border:1.3px solid #555;border-radius:5px;flex:none}
  .step .tx{font-size:4.6px;line-height:1.45;color:#555;width:84px}
  .step .tx b{color:#222}
  .grid{position:absolute;display:grid;grid-template-columns:repeat(3,1fr);gap:2px}
  .cell{height:68px;padding:14px 8px 6px;font-size:4.6px;line-height:1.4;color:#fff;position:relative}
  .cell b{display:block;margin-bottom:1px}
  .cell.red{background:var(--red)}
  .cell.dark{background:var(--grey)}
  .cell .plus{position:absolute;left:-7px;top:26px;width:12px;height:12px;border-radius:50%;background:#fff;color:var(--red);font-size:10px;font-weight:700;line-height:12px;text-align:center;z-index:1}
</style>
</head>
<body>

<!-- Cover A -->
<section class="panel" style="left:46px;top:75px;width:270px;height:271px">
  <div class="redbar" style="left:0;top:0;width:28px;height:271px"></div>
  <div class="abs waves-light" style="left:28px;top:0;width:126px;height:206px"></div>
  <div class="redbar" style="left:154px;top:0;width:4px;height:271px"></div>
  <div class="photo" role="img" aria-label="Primo piano di un contatore dell'acqua" style="left:158px;top:0;width:112px;height:271px"></div>
  <div class="abs name" style="left:40px;top:232px;font-size:18px">VELORA</div>
</section>
<section class="panel" style="left:322px;top:75px;width:271px;height:271px">
  <div class="abs name center" style="left:0;width:271px;top:76px;font-size:18px">VELORA</div>
  <div class="abs contact" style="left:0;width:271px;top:138px">
    <div class="socials"><span></span><span></span><span></span></div>velora-service.it
  </div>
  <div class="abs contact" style="left:0;width:271px;top:184px">VELORA S.r.l.<br>Via Lumera 12, 25100 Corvano<br>Tel 0300 000-000<br>velora-service.it<br>info@velora-service.it</div>
</section>
<div class="abs label" style="left:88px;top:356px">Cover (A)</div>

<!-- Cover B -->
<section class="panel waves-dark" style="left:606px;top:75px;width:272px;height:271px">
  <div class="abs name center on-dark" style="left:0;width:272px;top:181px;font-size:18px">VELORA</div>
  <div class="redbar" style="left:79px;top:258px;width:106px;height:13px"></div>
</section>
<section class="panel" style="left:883px;top:75px;width:271px;height:271px">
  <div class="abs name center" style="left:0;width:271px;top:76px;font-size:18px">VELORA</div>
  <div class="abs contact" style="left:0;width:271px;top:138px">
    <div class="socials"><span></span><span></span><span></span></div>velora-service.it
  </div>
  <div class="abs contact" style="left:0;width:271px;top:184px">VELORA S.r.l.<br>Via Lumera 12, 25100 Corvano<br>Tel 0300 000-000<br>velora-service.it<br>info@velora-service.it</div>
</section>
<div class="abs label" style="left:722px;top:356px">Cover (B)</div>

<!-- 01 Introduzione -->
<section class="panel" style="left:46px;top:418px;width:270px;height:272px">
  <div class="abs waves-dark" style="left:0;top:0;width:196px;height:272px"></div>
  <div class="abs" style="left:20px;top:82px;width:160px">
    <div class="num">01</div><div class="title">INTRODUZIONE</div><div class="dash"></div>
    <div class="body-text">
      <p>Siamo una società di servizi composta da un team di professionisti ed operatori specializzati.</p>
      <p>Offriamo soluzioni tecnologiche ed efficaci perché tempestive e performanti.</p>
      <p>VELORA nasce dalla richiesta del mercato di un soggetto nuovo, indipendente e soprattutto trasversale alle attuali realtà di settore. VELORA fornisce alle società di amministrazione condominiale un servizio professionale di lettura e riparto dei consumi acqua tempestivo, preciso ed efficace.</p>
    </div>
  </div>
  <div class="photo warm" role="img" aria-label="Tecnico con casco bianco al computer portatile" style="left:196px;top:0;width:74px;height:272px"></div>
</section>
<section class="panel" style="left:322px;top:418px;width:271px;height:272px">
  <div class="photo warm" role="img" aria-label="Tecnico al lavoro vicino ai contatori" style="left:0;top:0;width:100px;height:272px"></div>
  <div class="abs waves-fade" style="left:100px;top:0;width:171px;height:272px"></div>
  <div class="redbar" style="left:100px;top:32px;width:6px;height:106px"></div>
  <div class="illus" role="img" aria-label="Icona di un contatore con segnale di lettura a distanza" style="left:126px;top:36px;width:108px;height:108px"></div>
  <div class="abs" role="img" aria-label="Icone di edificio, impianto e goccia d'acqua" style="left:128px;top:180px;width:100px;height:30px;background:#e2e2e2"></div>
  <div class="foot-name name" style="left:216px;top:245px">VELORA</div>
</section>

<!-- 02 Servizio -->
<section class="panel" style="left:604px;top:418px;width:271px;height:272px">
  <div class="abs waves-dark" style="left:0;top:0;width:196px;height:272px"></div>
  <div class="abs" style="left:20px;top:82px;width:160px">
    <div class="num">02</div><div class="title">SERVIZIO</div><div class="dash"></div>
    <div class="body-text">
      <p>VELORA propone un servizio innovativo sul mercato, capace di gestire la lettura ed il riparto dei consumi acqua tramite un nuovo modello di service management.</p>
      <p>Abbiamo strutturato un servizio innovativo dedicato agli amministratori condominiali.</p>
      <p>Effettuiamo la lettura dei consumi reali dei contatori acqua relativi alle singole utenze private e comuni. Elaboriamo i dati raccolti in tempo reale e predisponiamo il riparto dei consumi acqua.</p>
    </div>
  </div>
  <div class="photo pipe" role="img" aria-label="Tubazione con contatore dell'acqua" style="left:196px;top:0;width:75px;height:272px"></div>
</section>
<section class="panel" style="left:878px;top:418px;width:272px;height:272px">
  <div class="photo" role="img" aria-label="Quadranti di un contatore dell'acqua" style="left:0;top:0;width:100px;height:272px"></div>
  <div class="abs waves-fade" style="left:100px;top:0;width:172px;height:272px"></div>
  <div class="redbar" style="left:100px;top:44px;width:6px;height:94px"></div>
  <div class="abs body-dark" style="left:119px;top:18px;width:140px">
    <p><b>Gli amministratori dispongono di uno strumento tecnico che consente la corretta ed immediata ripartizione dei consumi idrici.</b></p>
    <p>Il riparto dei consumi viene effettuato esclusivamente tramite letture reali, effettive e certificate delle singole utenze.</p>
    <p><b>NON effettuiamo servizi di bollettazione e riscossione.</b></p>
  </div>
  <div class="illus" role="img" aria-label="Icona di una persona collegata a una rete" style="left:163px;top:106px;width:62px;height:62px"></div>
  <div class="abs body-dark" style="left:119px;top:184px;width:140px">
    <p><b>VELORA promuove la campagna di sostituzione dei vecchi contatori con nuovi di ultima generazione abbinati al servizio di telelettura.</b></p>
    <p><b>L'offerta può essere modulata, a partire dalla sola fornitura dei nuovi contatori, sino alla consultazione dei dati per il singolo condominio con un'App dedicata.</b></p>
  </div>
  <div class="foot-name name" style="left:216px;top:245px">VELORA</div>
</section>

<!-- 03 Metodo -->
<section class="panel" style="left:46px;top:700px;width:270px;height:270px">
  <div class="abs waves-dark" style="left:0;top:0;width:196px;height:270px"></div>
  <div class="abs" style="left:20px;top:82px;width:160px">
    <div class="num">03</div><div class="title">METODO</div><div class="dash"></div>
    <div class="body-text"><p>VELORA agisce tramite un protocollo strategico definito.</p></div>
  </div>
  <svg class="abs" style="left:24px;top:186px" width="46" height="40" viewBox="0 0 46 40" aria-hidden="true">
    <g fill="none" stroke="#fff" stroke-width="1.2">
      <path d="M8 2a5 5 0 0 1 5 5c0 4-5 9-5 9s-5-5-5-9a5 5 0 0 1 5-5z"/>
      <path d="M30 8a8 8 0 0 1 8 8c0 7-8 14-8 14s-8-7-8-14a8 8 0 0 1 8-8z"/>
      <circle cx="30" cy="16" r="3"/>
      <path d="M8 20c0 6 4 14 16 16" stroke-dasharray="1.5 2"/>
    </g>
  </svg>
  <div class="abs body-text" style="left:78px;top:188px;width:92px"><p><b style="color:#fff">MAPPATURA:</b> attività preventiva di rilievo e raccolta dati delle singole utenze, posizionamento contatori e verifica criticità. Elaborazione della "Mappa Immobile" che sarà messa a disposizione dell'amministratore.</p></div>
  <div class="photo pipe" role="img" aria-label="Mani di un tecnico che installano un contatore" style="left:196px;top:0;width:74px;height:270px"></div>
</section>
<section class="panel" style="left:322px;top:700px;width:271px;height:270px">
  <div class="photo warm" role="img" aria-label="Operatore con casco e lampada frontale" style="left:0;top:0;width:100px;height:270px"></div>
  <div class="abs waves-fade" style="left:100px;top:0;width:171px;height:270px"></div>
  <div class="redbar" style="left:100px;top:108px;width:6px;height:104px"></div>
  <div class="step" style="left:124px;top:26px"><div class="ic"></div><div class="tx"><b>DATABASE:</b><br>costruzione del database degli immobili, delle utenze, delle letture consumi e di tutti i dati necessari al servizio.</div></div>
  <div class="step" style="left:124px;top:74px"><div class="ic"></div><div class="tx"><b>SCELTA CRITERI:</b><br>la modulazione dei criteri di lettura dei consumi può essere diversificata in base alle esigenze dei nostri clienti.</div></div>
  <div class="step" style="left:124px;top:124px"><div class="ic"></div><div class="tx"><b>ATTIVITA' LETTURA CONSUMI:</b><br>la lettura dei consumi delle singole utenze viene effettuata dai nostri operatori con modalità specifiche ed un supporto tecnologico innovativo.</div></div>
  <div class="step" style="left:124px;top:178px"><div class="ic"></div><div class="tx"><b>ELABORAZIONE DATI:</b><br>i dati raccolti dai nostri operatori vengono verificati ed elaborati consentendo la definizione del report di lettura e riparto dei consumi idrici degli immobili, tramite esportazione dati.</div></div>
  <div class="foot-name name" style="left:216px;top:245px">VELORA</div>
</section>

<!-- 04 Plus -->
<section class="panel" style="left:604px;top:700px;width:271px;height:270px">
  <div class="abs waves-dark" style="left:0;top:0;width:196px;height:270px"></div>
  <div class="abs" style="left:16px;top:82px;width:170px">
    <div class="num">04</div><div class="title">PLUS</div><div class="dash"></div>
    <div class="body-text"><p>VELORA dà valore aggiunto al servizio di amministrazione immobiliare con un grado maggiore di soddisfazione del cliente. Come? Grazie ad una struttura innovativa, tecnologie avanzate ed operatori specializzati.</p></div>
  </div>
  <div class="photo pipe" role="img" aria-label="Mani di un tecnico che installano un contatore" style="left:196px;top:0;width:75px;height:270px"></div>
</section>
<section class="panel" style="left:880px;top:700px;width:270px;height:270px">
  <div class="photo pipe" role="img" aria-label="Dettaglio di tubazione" style="left:0;top:0;width:18px;height:270px"></div>
  <div class="abs" style="left:26px;top:0;width:14px;height:270px;background:#c9c9c9"></div>
  <div class="abs waves-fade" style="left:40px;top:0;width:230px;height:270px"></div>
  <div class="grid" style="left:53px;top:70px;width:201px">
    <div class="cell red"><b>Assistenza</b>tempestiva e rapidità d'azione anche da remoto</div>
    <div class="cell dark"><span class="plus">+</span><b>Impegno minimo dell'utente</b>grazie al calendario delle letture in loco e/o gestione da remoto</div>
    <div class="cell dark"><span class="plus">+</span><b>Semplicità d'accesso ai servizi integrati</b>e risposta rapida alle esigenze dei clienti</div>
    <div class="cell dark"><b>Gestione "chiavi in mano"</b>dalla mappatura delle utenze fino al riparto dei consumi</div>
    <div class="cell dark"><span class="plus">+</span><b>Efficienza della Gestione</b>immobiliare in modo semplice, diretto e preciso</div>
    <div class="cell red"><span class="plus">+</span><b>Innovazione del servizio</b>Servizi innovativi, tecnologici e trasparenti per una migliore gestione dei patrimoni immobiliari</div>
  </div>
  <div class="foot-name name" style="left:211px;top:245px">VELORA</div>
</section>

</body>
</html>
```